Preisliste für Kosmetikinstitut
Zielgruppe
Ich benötige für mein Kosmetikinstitut eine Preisliste für die moderne Frau, aber auch Männer. Das Design sollte mein Logo enthalten. Farben des Designkonzepts einbauen.
A4 quer zum Falten, wie ein Heft, 1. Seite Preisliste mit logo, im Innenteil dann Anwendungen
Aufgabenstellung
Minimalistisch, ästhetisch, modern, edel
Kontaktdaten auf der Rückseite
LT Hautatelier
Lena Tessmar
Lindenstieg 17
83671 Ostermoor
EMail: lena@lt-hautatelier.de
Whatsapp: 0176 284 9017

```html
<!DOCTYPE html>
<html lang="de">
<head>
<meta charset="utf-8">
<title>LT Hautatelier – Preisliste</title>
<link rel="stylesheet" href="https://fonts.googleapis.com/css2?family=Questrial&display=swap">
<style>
  :root {
    --backdrop: #ffffff;
    --paper: #fbfbf3;
    --paper-tint: #f3f5ec;
    --ink: #6b7571;
    --gold: #c9a961;
  }
  * { margin: 0; padding: 0; box-sizing: border-box; }
  html, body {
    width: 1200px;
    height: 1200px;
    overflow: hidden;
    background: var(--backdrop);
    font-family: "Questrial", "Century Gothic", sans-serif;
  }
  .cover {
    position: absolute;
    left: 255px;
    top: 141px;
    width: 687px;
    height: 968px;
    background: var(--paper);
    box-shadow: 0 2px 14px rgba(0, 0, 0, 0.08);
    overflow: hidden;
  }
  .cover-pattern {
    position: absolute;
    inset: 0;
    background:
      radial-gradient(ellipse 260px 200px at 210px 170px, var(--paper-tint), transparent 70%),
      radial-gradient(ellipse 300px 160px at 520px 220px, var(--paper-tint), transparent 70%),
      radial-gradient(ellipse 280px 220px at 230px 470px, var(--paper-tint), transparent 70%),
      radial-gradient(ellipse 320px 240px at 480px 760px, var(--paper-tint), transparent 70%),
      radial-gradient(ellipse 200px 260px at 170px 800px, var(--paper-tint), transparent 70%);
  }
  .brand {
    position: absolute;
    left: 206px;
    top: 526px;
    display: flex;
    align-items: center;
    gap: 18px;
  }
  .brand-name {
    font-size: 30px;
    font-weight: 400;
    letter-spacing: 0.5px;
    color: var(--ink);
    white-space: nowrap;
  }
  .brand-mark {
    width: 96px;
    height: 96px;
    border: 2px solid var(--ink);
    border-radius: 50%;
    flex: none;
  }
  .cover-title {
    position: absolute;
    left: 656px;
    top: 404px;
    font-size: 34px;
    font-weight: 400;
    color: var(--gold);
    transform: rotate(90deg);
    transform-origin: left top;
    white-space: nowrap;
    letter-spacing: 0.5px;
  }
  .cover-dot {
    position: absolute;
    left: 333px;
    top: 902px;
    width: 24px;
    height: 24px;
    border-radius: 50%;
    background: var(--gold);
  }
</style>
</head>
<body>
  <main class="cover">
    <div class="cover-pattern" role="img" aria-label="Große, zarte Schriftzug-Dekoration im Hintergrund"></div>
    <div class="brand">
      <h1 class="brand-name">LT HAUTATELIER</h1>
      <span class="brand-mark"></span>
    </div>
    <p class="cover-title">Preisliste</p>
    <span class="cover-dot"></span>
  </main>
</body>
</html>
```